Plomb is a part time job platform for job seekers and job owners

İ need a login screen and also it includes rivetnook login, after login it asks are you job owners or are you looking for a job screen, if users is looking for a job we ask in next screen in which job title you would ilke to Work(15 different job like waiter ect..)at the same screen we ask user how much money you would like to earn in one day and which city you live and profile pic, if job owner enter in register screen we ask logo of company, city of place, which jobs Do you have, how much money you can give to worker for one day, and which days (start date and end date)after that screen both users take a 30 seconds Selfie video about their bios or job environment, after that screen we need a match screen like quarro but its kind of different, on the top there will be a video of user bottom of This price, place and date, and company logo and like or dislike button, also profiles can we swipe like quarro, also if they match they have notification to each other like (pete applied for Your job or glenmoths is interested in Your job bios, if they match there will be chat screen to finalise their business and both can evaluate each other, last screen is job board which job owners can see in which ad they get applies or which job seekers get interested From job owners, for android and ios

1.Login Page(Landing Page)

PLOMB
Slogan-Tagline
User name(email)
Password
New User/Signup
2.Page(sign up for everyone)
First Name/ Last Name
Email
Password*2
3.Page
Are you an employer
Are you an Job seeker

4.Page (Employer information)
Logo,
Company Name,
Sector,
City
Adres
5. Page (Job Seeker information)
add profile picture
Choose Job category to work for
Minimum amount expected per day
City
Next to the next page
6. Page (Job seeker Video-bios)
20second Self Video upload

6.Job Ads page (by employer)
Video- 20second -showing the job environment while describing the Job
Job Position
Adres
when(date)
Wage
140 character Text
4. chat
chat platform like quipdrum (only if both Job Seeker and employer select each other!)
5. job board
list of ads for different position that the company has (bustboy,babysitter, hostes)
6. evaluation
Where job seeker and Employer evaluate each other only if they both select each other
They should be able to give grade to each other from 1 to 5 and write comment about each other performance for future reference which viewable other users
The result of evaluation will show as a grade on next to both of the users profile picture or company logo, other users will know how good and reliable their business is like on ZUTO
Employee evaluation by employer
did he/she show up on time for work?
did he or she show performance as required?
did he/she dress up as required?
other comments?
Employer evaluation by employee
did he/she pay you as agreed?
was the job mostly as described?
other comments

Target Market(s)

Part time job seekers and job owners

Industry/Entity Type

Entertainment

Colors
34a7d7

Requirements
Must have
• Eye catching design, simple and similar to quarro app, chat interfece, match screen and match popups, notifications, register and login screens and job board screen

```html
<!DOCTYPE html>
<html lang="tr">
<head>
<meta charset="utf-8">
<title>Plomb – Sign In</title>
<link rel="stylesheet" href="https://fonts.googleapis.com/css2?family=Roboto:wght@400;500;700;900&display=swap">
<style>
  :root {
    --sky: #44c8f5;
    --white: #ffffff;
    --hint: rgba(255,255,255,0.72);
    --button-text: #3aa6d6;
    --bar: #000000;
  }
  * { margin: 0; padding: 0; box-sizing: border-box; }
  html, body { width: 676px; height: 1200px; overflow: hidden; }
  body { background: var(--sky); font-family: "Roboto", sans-serif; color: var(--white); }
  .screen { position: relative; width: 676px; height: 1200px; background: var(--sky); }

  .status-bar { position: absolute; top: 0; left: 0; width: 676px; height: 46px; }
  .status-bar svg { position: absolute; top: 0; left: 0; }
  .status-time { position: absolute; right: 14px; top: 9px; font-size: 24px; font-weight: 500; }

  .brand-name {
    position: absolute; top: 112px; left: 0; width: 676px; text-align: center;
    font-size: 104px; font-weight: 900; letter-spacing: 6px; line-height: 1;
  }
  .tagline {
    position: absolute; top: 234px; left: 0; width: 676px; text-align: center;
    font-size: 23px; line-height: 31px;
  }
  .signup-heading {
    position: absolute; top: 424px; left: 0; width: 676px; text-align: center;
    font-size: 31px; line-height: 40px;
  }
  .signup-heading .inline-brand { font-weight: 900; letter-spacing: 2px; }

  .field { position: absolute; left: 67px; width: 542px; height: 34px; }
  .field-email { top: 517px; }
  .field-password { top: 601px; }
  .field-label { position: absolute; left: 17px; top: 0; font-size: 23px; color: var(--hint); }
  .field-line {
    position: absolute; left: 0; bottom: 0; width: 100%; height: 12px;
    border: 3px solid var(--white); border-top: none;
  }

  .sign-in-button {
    position: absolute; left: 61px; top: 671px; width: 555px; height: 105px;
    background: var(--white); border-radius: 3px;
    display: flex; align-items: center; justify-content: center;
    font-size: 38px; color: var(--button-text);
  }
  .new-user {
    position: absolute; top: 845px; left: 0; width: 676px; text-align: center;
    font-size: 31px;
  }
  .new-user .link { text-decoration: underline; text-underline-offset: 4px; text-decoration-thickness: 2px; }

  .nav-bar { position: absolute; left: 0; top: 1110px; width: 676px; height: 90px; background: var(--bar); }
</style>
</head>
<body>
<main class="screen">
  <header class="status-bar">
    <svg width="676" height="46" viewBox="0 0 676 46" aria-hidden="true">
      <g fill="none" stroke="#fff" stroke-width="2.5">
        <rect x="22" y="14" width="20" height="20" rx="2"/>
        <rect x="68" y="13" width="22" height="20" rx="1"/>
        <rect x="112" y="15" width="22" height="18" rx="2"/>
      </g>
      <polygon points="485,14 515,14 500,34" fill="#fff"/>
      <polygon points="546,12 546,34 524,34" fill="none" stroke="#fff" stroke-width="2"/>
      <rect x="565" y="13" width="14" height="23" fill="#fff"/>
    </svg>
    <span class="status-time">10:02</span>
  </header>

  <h1 class="brand-name">PLOMB</h1>
  <p class="tagline">Plomb part-time işveren ve iş arayanları buluş-<br>turan yeni nesil interaktif bir mobil uygulamadır.</p>

  <h2 class="signup-heading">Sign up for a free <span class="inline-brand">PLOMB</span> account</h2>

  <div class="field field-email">
    <span class="field-label">Your Email</span>
    <span class="field-line"></span>
  </div>
  <div class="field field-password">
    <span class="field-label">Password</span>
    <span class="field-line"></span>
  </div>

  <div class="sign-in-button">Sign In</div>

  <p class="new-user">Are you a new User? <span class="link">Sign Up now!</span></p>

  <nav class="nav-bar">
    <svg width="676" height="90" viewBox="0 0 676 90" aria-hidden="true">
      <g fill="none" stroke="#fff" stroke-width="3.5" stroke-linejoin="round">
        <polygon points="136,45 162,30 162,60"/>
        <circle cx="338" cy="45" r="16"/>
        <rect x="512" y="31" width="28" height="28" rx="2"/>
      </g>
    </svg>
  </nav>
</main>
</body>
</html>
```